Business Card Design for Venture Lantern

Venture Lantern is a pro bono student consultancy service offered by Solvari KPTC to social start ups and enterprises. We provide consulting services with expertise in areas such as Marketing, IT, Business Strategy and Innovation.
I have attached\ the Venture Lantern Logo here for your perusal.
Industry/Entity Type
Business
Contact Information for Business Card
Name: Dae Hwan Park Name: Thomas Leung
Role: Project Leader Role: Vice Project Leader
M:0491203846 M: 0473560218
E: dae-hwan.park@solvarikptc.org E: thomas.leung@solvarikptc.org
W: www.solvarikptc.org W: www.solvarikptc.org

```html
<!DOCTYPE html>
<html lang="en">
<head>
<meta charset="utf-8">
<title>Venture Lantern – Business Card</title>
<link href="https://fonts.googleapis.com/css2?family=Barlow+Condensed:wght@300;400;600&display=swap" rel="stylesheet">
<style>
  :root {
    --ink: #111111;
    --paper: #ffffff;
    --accent: #f28c1c;
    --page: #ffffff;
    --shadow: rgba(0, 0, 0, 0.35);
  }
  * { margin: 0; padding: 0; box-sizing: border-box; }
  html, body {
    width: 1000px;
    height: 1200px;
    overflow: hidden;
    background: var(--page);
    font-family: "Barlow Condensed", "Arial Narrow", sans-serif;
    color: var(--ink);
  }
  .canvas { position: relative; width: 1000px; height: 1200px; }

  .card {
    position: absolute;
    left: 125px;
    width: 783px;
    height: 446px;
    box-shadow: 4px 6px 12px var(--shadow);
    overflow: hidden;
  }
  .card--front { top: 87px; background: var(--paper); }
  .card--back { top: 666px; background: var(--ink); }

  .wordmark {
    position: absolute;
    left: 26px;
    top: 24px;
    font-weight: 600;
    font-size: 40px;
    line-height: 36px;
    letter-spacing: 0.5px;
    text-transform: uppercase;
    color: var(--ink);
  }

  .person { position: absolute; top: 182px; }
  .person--left { left: 27px; text-align: left; }
  .person--right { right: 26px; text-align: right; }
  .person__name {
    font-weight: 400;
    font-size: 64px;
    line-height: 64px;
    letter-spacing: 0.5px;
  }
  .person__role {
    font-weight: 400;
    font-size: 27px;
    line-height: 28px;
    padding: 0 4px;
  }

  .divider {
    position: absolute;
    left: 25px;
    top: 287px;
    width: 738px;
    height: 2px;
    background: var(--ink);
  }

  .contact {
    position: absolute;
    display: flex;
    align-items: center;
    gap: 10px;
    font-weight: 400;
    font-size: 19px;
    letter-spacing: 0.6px;
  }
  .contact svg { display: block; fill: var(--ink); }
  .contact--phone-left { left: 30px; top: 304px; }
  .contact--mail-left { left: 25px; top: 344px; }
  .contact--phone-right { right: 20px; top: 304px; }
  .contact--mail-right { right: 18px; top: 344px; }

  .front-footer {
    position: absolute;
    left: 0;
    bottom: 0;
    width: 100%;
    height: 49px;
    border-top: 3px solid var(--accent);
    background: var(--ink);
  }
  .web {
    color: var(--paper);
    font-weight: 400;
    font-size: 28px;
    letter-spacing: 3.2px;
    text-align: center;
  }
  .front-footer .web { line-height: 46px; }

  .back-wordmark {
    position: absolute;
    left: 0;
    top: 146px;
    width: 100%;
    text-align: center;
    color: var(--paper);
    font-weight: 600;
    font-size: 82px;
    line-height: 80px;
    text-transform: uppercase;
    letter-spacing: 1px;
  }
  .back-footer {
    position: absolute;
    left: 0;
    top: 398px;
    width: 100%;
  }
</style>
</head>
<body>
<main class="canvas">

  <section class="card card--front" aria-label="Card front">
    <div class="wordmark">Venture<br>Lantern</div>

    <div class="person person--left">
      <div class="person__name">Dae Hwan Park</div>
      <div class="person__role">Project Leader</div>
    </div>
    <div class="person person--right">
      <div class="person__name">Thomas Leung</div>
      <div class="person__role">Vice Project Leader</div>
    </div>

    <div class="divider"></div>

    <div class="contact contact--phone-left">
      <svg width="18" height="28" viewBox="0 0 18 28" aria-hidden="true">
        <path d="M3 0h12a3 3 0 0 1 3 3v22a3 3 0 0 1-3 3H3a3 3 0 0 1-3-3V3a3 3 0 0 1 3-3zm0 3v19h12V3zM7.5 24h3v2h-3z"/>
      </svg>
      <span>0491203846</span>
    </div>
    <div class="contact contact--mail-left">
      <svg width="30" height="19" viewBox="0 0 30 19" aria-hidden="true">
        <path d="M0 0h30L15 10zM0 3l15 10L30 3v16H0z"/>
      </svg>
      <span>dae-hwan.park@solvarikptc.org</span>
    </div>

    <div class="contact contact--phone-right">
      <span>0473560218</span>
      <svg width="18" height="28" viewBox="0 0 18 28" aria-hidden="true">
        <path d="M3 0h12a3 3 0 0 1 3 3v22a3 3 0 0 1-3 3H3a3 3 0 0 1-3-3V3a3 3 0 0 1 3-3zm0 3v19h12V3zM7.5 24h3v2h-3z"/>
      </svg>
    </div>
    <div class="contact contact--mail-right">
      <span>thomas.leung@solvarikptc.org</span>
      <svg width="30" height="19" viewBox="0 0 30 19" aria-hidden="true">
        <path d="M0 0h30L15 10zM0 3l15 10L30 3v16H0z"/>
      </svg>
    </div>

    <footer class="front-footer">
      <div class="web">www.solvarikptc.org</div>
    </footer>
  </section>

  <section class="card card--back" aria-label="Card back">
    <div class="back-wordmark">Venture<br>Lantern</div>
    <div class="back-footer">
      <div class="web">www.solvarikptc.org</div>
    </div>
  </section>

</main>
</body>
</html>
```